Want a package created for a new protein bar

We would like a new package created for a new protein bar project The name of the bar will be VOLMBite a real food protein bar, we would like a ‘window’ on the package of bar like Brave Meadow bar below in images.

VOLMBite
‘Super Food Bar’
14g of Whey Protein
The package film size is the following 12cm width x 15cm Length,
Flavor Peanut Chocolate Chip, additional information will be attached shortly like nutrition facts,

Target Market(s)

fitness market, bodybuilders, athletes, everyday people

Industry/Entity Type

Health Product

Logo Text

VOLMBite

Font styles to use
Serif
Sans Serif
Decorative

Requirements
Must have
• Package window

```html
<!DOCTYPE html>
<html lang="en">
<head>
<meta charset="utf-8">
<title>VOLMBite Super Food Bar Wrapper</title>
<link rel="stylesheet" href="https://fonts.googleapis.com/css2?family=Arimo:wght@700&family=Oswald:wght@500&display=swap">
<style>
  :root {
    --orange: #f7941d;
    --red: #b20e10;
    --deep-red: #b5121b;
    --ink: #111111;
    --white: #ffffff;
    --stage: #e8e5e1;
    --nut-light: #e9c690;
    --nut-dark: #b98446;
  }
  html, body {
    margin: 0;
    width: 1200px;
    height: 1000px;
    overflow: hidden;
    background: var(--stage);
  }
  .canvas {
    position: relative;
    width: 1200px;
    height: 1000px;
  }
  .wrapper {
    position: absolute;
    left: 50px;
    top: 215px;
    width: 1100px;
    height: 570px;
    clip-path: path("M14,0 L1086,0 L1100,28.5 L1086,57 L1100,85.5 L1086,114 L1100,142.5 L1086,171 L1100,199.5 L1086,228 L1100,256.5 L1086,285 L1100,313.5 L1086,342 L1100,370.5 L1086,399 L1100,427.5 L1086,456 L1100,484.5 L1086,513 L1100,541.5 L1086,570 L14,570 L0,541.5 L14,513 L0,484.5 L14,456 L0,427.5 L14,399 L0,370.5 L14,342 L0,313.5 L14,285 L0,256.5 L14,228 L0,199.5 L14,171 L0,142.5 L14,114 L0,85.5 L14,57 L0,28.5 Z");
  }
  .pattern-field {
    position: absolute;
    inset: 0;
    background: linear-gradient(135deg, #c8741a 0%, #7a4410 55%, #3a2108 100%);
  }
  .top-strip {
    position: absolute;
    left: 487px;
    top: 40px;
    width: 363px;
    height: 60px;
    background: var(--orange);
  }
  .brand-band {
    position: absolute;
    left: 14px;
    top: 100px;
    width: 836px;
    height: 170px;
    background: var(--red);
    display: flex;
    align-items: center;
    justify-content: center;
  }
  .brand-name {
    font-family: "Arimo", Arial, sans-serif;
    font-weight: 700;
    font-size: 92px;
    color: var(--white);
    letter-spacing: 1px;
  }
  .tagline-band {
    position: absolute;
    left: 14px;
    top: 270px;
    width: 836px;
    height: 80px;
    background: var(--orange);
    display: flex;
    align-items: center;
    justify-content: center;
  }
  .tagline {
    font-family: "Arimo", Arial, sans-serif;
    font-weight: 700;
    font-size: 50px;
    color: var(--deep-red);
  }
  .protein-claim {
    position: absolute;
    left: 181px;
    top: 398px;
    font-family: "Arimo", Arial, sans-serif;
    font-weight: 700;
    font-size: 19px;
    color: var(--white);
    -webkit-text-stroke: 0.6px var(--ink);
    paint-order: stroke fill;
  }
  .flavor-box {
    position: absolute;
    left: 487px;
    top: 352px;
    width: 352px;
    height: 148px;
    background: var(--white);
    border: 4px solid var(--red);
    border-radius: 16px;
    display: flex;
    flex-direction: column;
    align-items: center;
    justify-content: center;
    font-family: "Oswald", "Arial Narrow", sans-serif;
    font-weight: 500;
    font-size: 46px;
    line-height: 1.15;
    color: var(--ink);
    text-transform: uppercase;
  }
  .bar-window {
    position: absolute;
    left: 850px;
    top: 40px;
    width: 219px;
    height: 508px;
    background: linear-gradient(160deg, var(--nut-light) 0%, #d9a865 50%, var(--nut-dark) 100%);
  }
</style>
</head>
<body>
<main class="canvas">
  <section class="wrapper">
    <div class="pattern-field" role="img" aria-label="Orange and black zigzag pattern"></div>
    <div class="top-strip"></div>
    <div class="brand-band">
      <span class="brand-name">VOLMBite</span>
    </div>
    <div class="tagline-band">
      <span class="tagline">SUPER FOOD BAR</span>
    </div>
    <span class="protein-claim">14g of Whey Protein</span>
    <div class="flavor-box">
      <span>Flavor&nbsp; Peanut</span>
      <span>Chocolate Chip</span>
    </div>
    <div class="bar-window" role="img" aria-label="Window showing the peanut chocolate chip bar inside"></div>
  </section>
</main>
</body>
</html>
```